my website is tabellepiece.com. (brand name is ta belle pièce) This is just a template that i have choose for. The content and the pictures are not about my business just the template.
I would like to have 4 pages for now. 1 homepage, which will be an overview for all pages, it is right now in this way. It will directly highlight my story. My website will tell an exclusive story about details which makes the difference and will make people happy with very small things. It will be art related but very stylish as well. I also want to have a event agenda on my homepage where people can see where my next event is. Page 2 my blog, where I will write weekly about mindset, lifestyle and details. Inspiration place for people who are looking for unique and exclusive approaches in life. Page 3 shop, where I will sell my stuff which is handmade and unique, it will be limited edition stuff. Mostly I will make the designs from marbling art, which I am a teacher for. (https://www.vidorastream.com/watch?v=Kq7TbWm2Xa) check this video out for more. Page 4 is book page. Here people will be able to book private or group classes for marbling art (check the video). I have already a community of more than 500 people on join ring, which will be my public as well. I wanna implement the join ring button on this page as well. to be able to track.

This is about my website. I also need a logo for my brand, which will suit my website and my goals.

I can also give you a reference website, which really like as structure and style;
https://www.brightmorrowco.com/products/the-daybook-organizer?ref=Xp4RtLm8QzVw2NbKc7HsJd9FgTy3MvEqBa6WnUoZr1LkPxYhGiCe5DsAtQfVbNj0HmRwKyXo8LcTpZaEsUv2GqDnIwMb

ta belle pièce

4 page

• I can also give you a reference website, which really like as structure and style;
• https://www.brightmorrowco.com/products/the-daybook-organizer?ref=Xp4RtLm8QzVw2NbKc7HsJd9FgTy3MvEqBa6WnUoZr1LkPxYhGiCe5DsAtQfVbNj0HmRwKyXo8LcTpZaEsUv2GqDnIwMb

```html
<!DOCTYPE html>
<html lang="en">
<head>
<meta charset="utf-8">
<title>ta belle pièce</title>
<link rel="stylesheet" href="https://fonts.googleapis.com/css2?family=DM+Serif+Display&family=Domine:wght@400&family=Lato:wght@400;700&display=swap">
<style>
:root{
  --ink:#2b2b2b;
  --text:#3a3a3a;
  --muted:#555;
  --gold:#d89a3c;
  --beige:#f2e0cf;
  --white:#ffffff;
  --dark:#303030;
  --line:#e3e3e3;
}
*{box-sizing:border-box;margin:0;padding:0}
html,body{width:1200px;height:3209px;overflow:hidden;background:var(--white)}
body{position:relative;font-family:"Domine",Georgia,serif;color:var(--text)}
a{text-decoration:none}
.abs{position:absolute}
.serif{font-family:"DM Serif Display",Georgia,serif;font-weight:400}

/* nav */
.site-nav{left:0;top:0;width:1200px;height:75px;background:var(--white)}
.nav-link{top:30px;font-family:"Lato",Arial,sans-serif;font-size:11px;letter-spacing:.5px;color:var(--ink)}
.brand{left:0;width:1200px;top:14px;text-align:center;font-size:33px;color:var(--ink)}

/* hero */
.hero-art{left:0;top:75px;width:1200px;height:413px;
  background:
   radial-gradient(ellipse 260px 160px at 180px 130px,#2f9e7a 0,transparent 70%),
   radial-gradient(ellipse 300px 170px at 560px 110px,#e8d21e 0,transparent 70%),
   radial-gradient(ellipse 320px 180px at 900px 150px,#b94a9c 0,transparent 70%),
   radial-gradient(ellipse 260px 160px at 420px 330px,#d0649e 0,transparent 70%),
   radial-gradient(ellipse 300px 150px at 1000px 360px,#f0d8a8 0,transparent 70%),
   linear-gradient(100deg,#7a5a8c,#c7a24a 45%,#c08ac0 80%,#e9dccb)}
.hero-title{left:173px;top:172px;font-size:56px;line-height:64px;color:var(--white)}
.hero-copy{left:173px;top:266px;width:495px;font-size:11px;line-height:17px;color:var(--white)}
.btn-dark{display:block;text-align:center;background:var(--dark);color:var(--white);font-family:"Lato",Arial,sans-serif;font-size:10px;letter-spacing:.6px;line-height:34px;height:34px}
.btn-line{display:block;text-align:center;border:1.5px solid var(--gold);color:var(--gold);font-family:"Lato",Arial,sans-serif;font-size:10px;letter-spacing:.6px;background:var(--white)}

/* headings */
.section-title{font-size:27px;line-height:34px;color:var(--ink)}
.rule{height:2px;width:114px;background:var(--gold)}
.body-copy{font-size:11px;line-height:17.5px;color:var(--muted)}

/* about */
.portrait{left:612px;top:563px;width:415px;height:387px;background:linear-gradient(160deg,#8a7a66,#5e4b3c 55%,#a8432e)}
.frame{border:1.5px solid rgba(255,255,255,.75)}

/* blog */
.band{left:0;top:1253px;width:1200px;height:794px;background:linear-gradient(135deg,#f4e3d3,#eed7c2 60%,#f3e2d2)}
.card-image{background:linear-gradient(150deg,#2f3228,#4a4a3c 50%,#2c2d26)}
.card-image.two{background:linear-gradient(150deg,#3a2f2f,#5a4b46 50%,#4b3a3c)}
.card-image h3{position:absolute;left:34px;right:34px;text-align:center;color:var(--white);font-size:25px;line-height:30px}
.card-text{background:var(--white);box-shadow:0 6px 20px rgba(0,0,0,.12)}
.card-frame{border:1.5px solid var(--gold)}
.post-date{font-family:"Domine",Georgia,serif;font-size:15px;color:var(--ink)}

/* products */
.product-img{top:2190px;width:270px;height:270px}
.product-name,.price{top:2476px;font-family:"Domine",Georgia,serif;font-size:16px;color:var(--ink)}
.price{text-align:right}

/* events */
.events-bg{left:0;top:2770px;width:1200px;height:439px;background:linear-gradient(160deg,#3e3c3a,#2a2928 50%,#353331)}
.events-table{left:173px;top:2695px;width:854px;background:var(--white);border-collapse:collapse;box-shadow:0 6px 20px rgba(0,0,0,.2)}
.events-table th{background:var(--dark);color:var(--white);font-family:"Domine",Georgia,serif;font-weight:400;font-size:15px;height:75px;text-align:left}
.events-table td{height:75px;font-family:"Domine",Georgia,serif;font-size:15px;color:var(--ink);border-bottom:1px solid var(--line)}
.events-table tr:last-child td{border-bottom:0}
.events-table sup,.events-table sub{font-size:9px}
.events-table .btn-line{width:114px;height:36px;line-height:33px;margin-left:auto;margin-right:30px}
.footer-note{left:173px;top:3134px;font-size:11px;color:#ddd}
.social{top:3134px;width:12px;height:12px;border-radius:50%;background:#eee}
</style>
</head>
<body>

<header class="abs site-nav">
  <a class="abs nav-link" style="left:327px" href="#">HOME</a>
  <a class="abs nav-link" style="left:402px" href="#">BLOG</a>
  <div class="abs brand serif">ta belle pièce</div>
  <a class="abs nav-link" style="left:768px" href="#">SHOP</a>
  <a class="abs nav-link" style="left:838px" href="#">BOOK</a>
</header>

<section>
  <div class="abs hero-art" role="img" aria-label="Blurred close-up of colourful marbled paint"></div>
  <h1 class="abs hero-title serif">ta belle pièce</h1>
  <p class="abs hero-copy">Lorem ipsum dolor sit amet, consectetuer adipiscing elit, sed diam nonummy nibh euis-mod tincidunt ut laoreet dolore magna aliquam erat volutpat. Ut wisi enim ad minim veniam.</p>
  <a class="abs btn-dark" style="left:173px;top:349px;width:111px" href="#">LEARN MORE</a>
</section>

<section>
  <h2 class="abs section-title serif" style="left:173px;top:556px">About the Artist</h2>
  <div class="abs rule" style="left:173px;top:606px"></div>
  <p class="abs body-copy" style="left:173px;top:628px;width:418px">Lorem ipsum dolor sit amet, consectetuer adipiscing elit, sed diam nonummy nibh euismod tincidunt ut laoreet dolore magna aliquam erat volutpat.</p>
  <p class="abs body-copy" style="left:173px;top:698px;width:418px">Ut wisi enim ad minim veniam, quis nostrud exerci tation ullam corper suscipit lobortis nisl ut aliquip ex ea commodo consequat. Duis autem vel eum iriure dolor in hendrerit in vulputate velit esse moles tie consequat, vel illum dolore eu feugiat nulla facilisis at vero eros et accumsan et iusto odio dignissim qui blandit praesent luptatum zzril de lenit augue duis dolore te feugait nulla facilisi.</p>
  <p class="abs body-copy" style="left:173px;top:825px;width:418px">Investigationes demonstraverunt lectores legere me lius quod ii legunt saepius. Claritas est etiam processus dynamicus, qui sequitur mutationem consuetudium lectorum.</p>
  <a class="abs btn-line" style="left:173px;top:915px;width:111px;height:35px;line-height:32px" href="#">LEARN MORE</a>
  <div class="abs portrait" role="img" aria-label="Portrait photograph of the artist"></div>
  <div class="abs frame" style="left:624px;top:575px;width:391px;height:363px"></div>
</section>

<section>
  <div class="abs band" role="img" aria-label="Soft beige marbled paper texture"></div>
  <h2 class="abs section-title serif" style="left:0;width:1200px;text-align:center;top:1094px">From the Blog</h2>
  <div class="abs rule" style="left:543px;top:1143px"></div>

  <article>
    <div class="abs card-image" style="left:173px;top:1172px;width:428px;height:342px" role="img" aria-label="Photograph of a leafy garden terrace">
      <div class="abs frame" style="left:14px;top:14px;right:14px;bottom:14px"></div>
      <h3 class="serif" style="top:106px">Duis autem vel eum iriure dolor in hendrerit in vulputate velit esse molestie consequat vel illum dolore</h3>
    </div>
    <div class="abs card-text" style="left:601px;top:1172px;width:426px;height:342px">
      <div class="abs card-frame" style="left:14px;top:12px;right:14px;bottom:12px"></div>
      <p class="abs post-date" style="left:30px;top:55px">Oct 09, 2017</p>
      <p class="abs body-copy" style="left:30px;top:98px;width:370px">Lorem ipsum dolor sit amet, consectetuer adipiscing elit, sed diam nonummy nibh euismod tincidunt ut laoreet dolore magna aliquam erat volutpat.  Ut wisi enim ad minim veniam, quis no strud exerci tation ullam corper suscipit lobortis nisl ut aliquip ex ea commodo consequat. Duis autem vel eum iriure dolor in hendrerit in vulputate velit esse molestie consequat facilisi.</p>
      <a class="abs btn-line" style="left:30px;top:246px;width:111px;height:37px;line-height:34px" href="#">READ MORE</a>
    </div>
  </article>

  <article>
    <div class="abs card-text" style="left:173px;top:1553px;width:428px;height:342px">
      <div class="abs card-frame" style="left:14px;top:12px;right:14px;bottom:12px"></div>
      <p class="abs post-date" style="left:30px;top:53px">Oct 09, 2017</p>
      <p class="abs body-copy" style="left:30px;top:96px;width:370px">Lorem ipsum dolor sit amet, consectetuer adipiscing elit, sed diam nonummy nibh euismod tincidunt ut laoreet dolore magna aliquam erat volutpat.  Ut wisi enim ad minim veniam, quis no strud exerci tation ullam corper suscipit lobortis nisl ut aliquip ex ea commodo consequat. Duis autem vel eum iriure dolor in hendrerit in vulputate velit esse molestie consequat facilisi.</p>
      <a class="abs btn-line" style="left:30px;top:244px;width:111px;height:37px;line-height:34px" href="#">READ MORE</a>
    </div>
    <div class="abs card-image two" style="left:601px;top:1553px;width:426px;height:342px" role="img" aria-label="Photograph of paint jars above a marbled sheet">
      <div class="abs frame" style="left:14px;top:14px;right:14px;bottom:14px"></div>
      <h3 class="serif" style="top:106px">Mirum est notare quam littera gothica, quam nunc putamus parum claram, anteposuerit litterarum</h3>
    </div>
  </article>

  <a class="abs btn-dark" style="left:543px;top:1936px;width:112px" href="#">VIEW ALL</a>
</section>

<section>
  <h2 class="abs section-title serif" style="left:0;width:1200px;text-align:center;top:2112px">Featured Products</h2>
  <div class="abs rule" style="left:543px;top:2164px"></div>

  <div class="abs product-img" style="left:173px;background:linear-gradient(135deg,#f4d23a,#e25a9c 35%,#3c8fd0 60%,#f2a0c0 85%)" role="img" aria-label="Marbled paper in pink, yellow and blue"></div>
  <p class="abs product-name" style="left:173px">Product 1</p>
  <p class="abs price" style="left:343px;width:100px">$500.00</p>
  <a class="abs btn-line" style="left:251px;top:2515px;width:114px;height:35px;line-height:32px" href="#">ADD TO CART</a>

  <div class="abs product-img" style="left:464px;background:linear-gradient(135deg,#d8302a,#4aa8a0 35%,#e8c030 55%,#c8242a 80%)" role="img" aria-label="Marbled paper in red, teal and yellow"></div>
  <p class="abs product-name" style="left:464px">Product 2</p>
  <p class="abs price" style="left:634px;width:100px">$500.00</p>
  <a class="abs btn-line" style="left:542px;top:2515px;width:114px;height:35px;line-height:32px" href="#">ADD TO CART</a>

  <div class="abs product-img" style="left:757px;background:linear-gradient(135deg,#b08a2a,#2a3a6a 40%,#c9cfe0 60%,#9c7a20 85%)" role="img" aria-label="Marbled paper in ochre, navy and pale blue"></div>
  <p class="abs product-name" style="left:757px">Product 3</p>
  <p class="abs price" style="left:927px;width:100px">$500.00</p>
  <a class="abs btn-line" style="left:836px;top:2515px;width:114px;height:35px;line-height:32px" href="#">ADD TO CART</a>
</section>

<section>
  <div class="abs events-bg" role="img" aria-label="Dim photograph of a marbling workshop table"></div>
  <h2 class="abs section-title serif" style="left:0;width:1200px;text-align:center;top:2617px">Upcoming Events</h2>
  <div class="abs rule" style="left:543px;top:2668px"></div>

  <table class="abs events-table">
    <thead>
      <tr><th style="padding-left:30px;width:236px">Date</th><th style="width:284px">Venue</th><th style="width:190px">Time</th><th></th></tr>
    </thead>
    <tbody>
      <tr><td style="padding-left:30px">20<sup>th</sup> October, 2017</td><td>Nam liber tempor soluta</td><td>10:00<sub>AM</sub> - 01:00<sub>PM</sub></td><td><a class="btn-line" href="#">VIEW DETAILS</a></td></tr>
      <tr><td style="padding-left:30px">20<sup>th</sup> October, 2017</td><td>Nam liber tempor soluta</td><td>10:00<sub>AM</sub> - 01:00<sub>PM</sub></td><td><a class="btn-line" href="#">VIEW DETAILS</a></td></tr>
      <tr><td style="padding-left:30px">20<sup>th</sup> October, 2017</td><td>Nam liber tempor soluta</td><td>10:00<sub>AM</sub> - 01:00<sub>PM</sub></td><td><a class="btn-line" href="#">VIEW DETAILS</a></td></tr>
      <tr><td style="padding-left:30px">20<sup>th</sup> October, 2017</td><td>Nam liber tempor soluta</td><td>10:00<sub>AM</sub> - 01:00<sub>PM</sub></td><td><a class="btn-line" href="#">VIEW DETAILS</a></td></tr>
    </tbody>
  </table>
</section>

<footer>
  <p class="abs footer-note">Copyright ta belle pièce ©</p>
  <span class="abs social" style="left:869px"></span>
  <span class="abs social" style="left:912px"></span>
  <span class="abs social" style="left:957px"></span>
  <span class="abs social" style="left:1001px"></span>
</footer>

</body>
</html>
```